Private Optometric Practice Needs new Presentation Folders/Stationary

We recently moved our office and are looking to refresh our presentation folders and stationary. I tend to prefer simple, clean designs. We are a full scope optometric practice provide high quality eyewear, custom contact lenses, along with emergency care and treatment for dry eyes. We communicate with a lot of other doctors and want to exude professionalism. I have attached 2 versions of our logo.

Target Market(s)

Familys

Industry/Entity Type

Eyecare

Font styles to use
Sans Serif

Colors
0054AA
0677BA
7BADD7
CADEEF
E8F1F8

Requirements
Nice to have
• Bifold, areas to put information about practice, welcome letter

```html
<!DOCTYPE html>
<html lang="en">
<head>
<meta charset="utf-8">
<title>Northfield Vision – Business Card</title>
<link href="https://fonts.googleapis.com/css2?family=Open+Sans:wght@400;600;700&display=swap" rel="stylesheet">
<style>
  :root {
    --stage: #232323;
    --card-blue: #3aa8e0;
    --card-blue-deep: #1f8cca;
    --card-navy: #0a1824;
    --accent: #38a6e0;
    --ink-light: #ffffff;
    --ink-soft: #e6eef5;
  }
  * { margin: 0; padding: 0; box-sizing: border-box; }
  html, body {
    width: 1200px; height: 780px; overflow: hidden;
    background: var(--stage);
    font-family: "Open Sans", Arial, sans-serif;
  }
  .stage { position: relative; width: 1200px; height: 780px; }

  .card {
    position: absolute;
    width: 560px; height: 320px;
    border-radius: 26px;
    overflow: hidden;
  }

  /* Front */
  .card--front {
    left: 60px; top: 70px;
    background: var(--card-blue);
    display: flex; align-items: center; justify-content: center;
  }
  .front-brand {
    display: flex; flex-direction: column; align-items: center; gap: 14px;
    color: var(--card-blue-deep);
  }
  .front-brand__dot {
    width: 70px; height: 70px; border-radius: 50%;
    background: var(--card-blue-deep);
  }
  .front-brand__name {
    font-weight: 600; font-size: 40px; letter-spacing: 10px;
    text-transform: uppercase; text-align: center; line-height: 1.15;
  }

  /* Back */
  .card--back {
    left: 580px; top: 390px;
    background: var(--card-navy);
    border-bottom: 4px solid var(--accent);
    display: flex; align-items: center;
    padding: 0 34px;
  }
  .back-brand {
    width: 210px;
    display: flex; flex-direction: column; align-items: center; gap: 12px;
    color: var(--ink-light);
  }
  .back-brand__dot {
    width: 50px; height: 50px; border-radius: 50%;
    background: var(--accent);
  }
  .back-brand__name {
    font-weight: 600; font-size: 24px; letter-spacing: 6px;
    text-transform: uppercase; text-align: center; line-height: 1.2;
  }
  .divider {
    width: 1px; height: 170px; background: var(--accent);
    margin: 0 26px;
  }
  .contact { color: var(--ink-soft); }
  .contact__name {
    color: var(--accent); font-weight: 700; font-size: 22px;
    text-transform: uppercase; line-height: 1.1;
  }
  .contact__role { font-size: 14px; margin-bottom: 14px; }
  .contact__list { list-style: none; font-size: 13px; line-height: 1.55; }
  .contact__list li { display: flex; align-items: center; gap: 8px; }
  .contact__list svg { width: 13px; height: 13px; fill: var(--accent); flex: none; }
  .contact__address { font-size: 13px; line-height: 1.5; margin-top: 12px; }
</style>
</head>
<body>
<main class="stage">

  <section class="card card--front" aria-label="Card front">
    <div class="front-brand">
      <span class="front-brand__dot"></span>
      <p class="front-brand__name">Northfield<br>Vision</p>
    </div>
  </section>

  <section class="card card--back" aria-label="Card back">
    <div class="back-brand">
      <span class="back-brand__dot"></span>
      <p class="back-brand__name">Northfield<br>Vision</p>
    </div>
    <span class="divider"></span>
    <div class="contact">
      <h1 class="contact__name">Daniel Harper</h1>
      <p class="contact__role">Managing Director</p>
      <ul class="contact__list">
        <li>
          <svg viewBox="0 0 24 24"><path d="M6.6 10.8a15.1 15.1 0 0 0 6.6 6.6l2.2-2.2a1 1 0 0 1 1-.25 11.4 11.4 0 0 0 3.6.57 1 1 0 0 1 1 1V20a1 1 0 0 1-1 1A17 17 0 0 1 3 4a1 1 0 0 1 1-1h3.5a1 1 0 0 1 1 1c0 1.25.2 2.45.57 3.57a1 1 0 0 1-.25 1z"/></svg>
          123 456 789
        </li>
        <li>
          <svg viewBox="0 0 24 24"><path d="M2 5h20v14H2zm2 2v.4l8 5.1 8-5.1V7zm0 2.8V17h16V9.8l-8 5.1z"/></svg>
          info@yourgmail.com
        </li>
        <li>
          <svg viewBox="0 0 24 24"><path d="M12 2a10 10 0 1 0 0 20 10 10 0 0 0 0-20zm6.9 6h-2.9a15 15 0 0 0-1.3-3.6A8 8 0 0 1 18.9 8zM12 4c.8 1.2 1.5 2.5 1.9 4h-3.8c.4-1.5 1.1-2.8 1.9-4zM4.3 14a8 8 0 0 1 0-4h3.4a16 16 0 0 0 0 4zm.8 2h2.9c.3 1.3.8 2.5 1.3 3.6A8 8 0 0 1 5.1 16zM8 8H5.1a8 8 0 0 1 4.3-3.6C8.8 5.5 8.4 6.7 8 8zm4 12c-.8-1.2-1.5-2.5-1.9-4h3.8c-.4 1.5-1.1 2.8-1.9 4zm2.3-6H9.7a14 14 0 0 1 0-4h4.6a14 14 0 0 1 0 4zm.3 5.6c.5-1.1 1-2.3 1.3-3.6h2.9a8 8 0 0 1-4.2 3.6zm1.7-5.6a16 16 0 0 0 0-4h3.4a8 8 0 0 1 0 4z"/></svg>
          www.yourwebsite.com
        </li>
      </ul>
      <p class="contact__address">Your address, City<br>State, Zip 1234</p>
    </div>
  </section>

</main>
</body>
</html>
```